Web Page Template and Logo Design

We are launching a website to sell homewares and would like a logo design, as well as a home page template, and the template for the product pages.

The homewares store is called Saucy Newt. The homewares we will sell will be edgy and very bright colours. We envisage the theme of the homepage will have hot pink, some blue/ white chinioserie pattern and potentially lime green. We would like the logo to reflect humour and "Saucy Newt".

The images uploaded reflect the look and feel of the type of people who are our customers - they are not minimalists and they are definitely not into beige!

Target Market(s)

Predominantly women, 30 - 50

Industry/Entity Type

Store

Number of Pages Required

2 page

Font styles to use
Sans Serif

Colors
e34197
acd036
33a6d7

Requirements
Must have
• Template for home page and standard template for other pages;PLEASE NOTE: I have now listed the Saucy Newt Logo as a separate 2 day listing; a bright, bold, colourful website with a sense of humour (it needs to dare people to put something bright in their homes).
• Please Note: I don't need a whole website, I have one of my staff who can do that for me. I just want the creative template for the homepage and a standard template for the product pages. It is the graphic design and creative side I am more interested in. I will want my staff member to be able to take the design and incorporate it into the website.

```html
<!DOCTYPE html>
<html lang="en">
<head>
<meta charset="utf-8">
<title>Saucy Newt – Products</title>
<link rel="stylesheet" href="https://fonts.googleapis.com/css2?family=ABeeZee&family=Roboto:wght@400;500&family=Roboto+Condensed:ital,wght@1,300&display=swap">
<style>
  :root {
    --header-bg: #ececec;
    --nav-text: #3a2040;
    --nav-active: #9b1a9b;
    --brand-pink: #d8409a;
    --panel-bg: #eeeeee;
    --ink-navy: #1c1c3c;
    --ink-plum: #4a0f4a;
    --footer-bg: #520f52;
    --footer-muted: #bfa0bf;
    --rule: #9a9a9a;
    --white: #ffffff;
  }
  * { margin: 0; padding: 0; box-sizing: border-box; }
  html, body { width: 1012px; height: 1200px; overflow: hidden; }
  body { position: relative; font-family: "Roboto", Arial, sans-serif; background: #f4eef0; }

  .hero-backdrop {
    position: absolute; left: 0; top: 0; width: 1012px; height: 1200px;
    background:
      radial-gradient(ellipse 180px 160px at 410px 180px, #f4f1f2 0%, rgba(244,241,242,0) 70%),
      linear-gradient(90deg, #e98cbd 0%, #ee9fc8 45%, #f3c6dc 70%, #f5f1f0 85%, #f2eeec 100%);
  }
  .hero-backdrop::after {
    content: ""; position: absolute; left: 0; right: 0; bottom: 0; height: 300px;
    background: linear-gradient(180deg, rgba(190,120,100,0) 0%, #b26a4f 100%);
  }

  .site-header { position: absolute; left: 0; top: 0; width: 1012px; height: 61px; background: var(--header-bg); }
  .brand-name {
    position: absolute; left: 134px; top: 52px;
    font: 500 36px/1 "Roboto", Arial, sans-serif; color: var(--brand-pink);
  }
  .brand-dot { position: absolute; left: 140px; top: 14px; width: 26px; height: 26px; border-radius: 50%; background: var(--brand-pink); }
  .main-nav a {
    position: absolute; top: 5px; height: 56px;
    font: 400 10.5px/56px "Roboto", Arial, sans-serif; text-transform: uppercase;
    color: var(--nav-text); text-decoration: none; text-align: center;
  }
  .main-nav a.is-active { background: var(--nav-active); color: var(--white); }

  .tagline {
    position: absolute; left: 131px; top: 140px; width: 750px;
    border-top: 4px dotted #6a4a60; border-bottom: 4px dotted #6a4a60;
    padding: 0 0 1px;
    font: italic 300 30px/28px "Roboto Condensed", Arial, sans-serif; color: #4a1a4a;
    text-align: center;
  }

  .content-panel {
    position: absolute; left: 126px; top: 302px; width: 759px; height: 665px;
    background: var(--panel-bg); box-shadow: 0 0 14px rgba(0,0,0,0.25);
  }
  .breadcrumb { position: absolute; left: 40px; top: 22px; font-size: 10.5px; color: #333; }
  .breadcrumb-rule { position: absolute; left: 40px; top: 45px; width: 680px; border-top: 1px solid var(--rule); }
  .page-title {
    position: absolute; left: 0; top: 67px; width: 759px; text-align: center;
    font: 400 26px/1.2 "ABeeZee", Arial, sans-serif; color: var(--ink-navy);
  }
  .intro {
    position: absolute; left: 44px; top: 152px; width: 668px;
    font-size: 19.5px; line-height: 24px; color: var(--ink-plum); text-indent: 42px;
  }
  .feature-heading {
    position: absolute; left: 44px; top: 296px;
    font: 400 41px/1.2 "Roboto", Arial, sans-serif; color: var(--ink-plum);
  }
  .dotted-rule { position: absolute; left: 44px; top: 362px; width: 672px; border-top: 3px dotted #8a8a8a; }
  .service-card { position: absolute; top: 403px; width: 210px; }
  .service-card h2 { font: 400 26px/1.2 "ABeeZee", Arial, sans-serif; color: var(--ink-navy); margin-bottom: 13px; }
  .service-card p { font-size: 12.4px; line-height: 19px; text-align: justify; color: var(--ink-plum); }

  .site-footer {
    position: absolute; left: 126px; top: 967px; width: 759px; height: 233px;
    background: var(--footer-bg); color: var(--white);
  }
  .social-links { position: absolute; left: 340px; top: 24px; width: 80px; height: 24px; }
  .contact-block { position: absolute; left: 0; top: 60px; width: 759px; text-align: center; font-size: 13.5px; line-height: 19px; }
  .footnote { position: absolute; left: 40px; top: 174px; font-size: 10.5px; color: var(--footer-muted); }
  .footnote sup { font-size: 7px; }
  .site-footer a { color: var(--white); }
  .footer-links { position: absolute; left: 40px; top: 200px; font-size: 10.5px; color: var(--footer-muted); }
  .login-link { position: absolute; right: 36px; top: 200px; font-size: 10.5px; }
</style>
</head>
<body>
  <div class="hero-backdrop" role="img" aria-label="Softly blurred interior photo: hot pink patterned wallpaper, round mirror, blue and white vases and a painted chair"></div>

  <header class="site-header">
    <nav class="main-nav">
      <a class="is-active" href="#" style="left:552px;width:91px;">Products</a>
      <a href="#" style="left:651px;width:70px;">Gallery</a>
      <a href="#" style="left:731px;width:80px;">About us</a>
      <a href="#" style="left:822px;width:88px;">Contact us</a>
    </nav>
  </header>
  <span class="brand-dot"></span>
  <div class="brand-name">Saucy Newt</div>

  <blockquote class="tagline">"If you dare nothing, then when the day is over, nothing is all you will have gained."</blockquote>

  <main class="content-panel">
    <div class="breadcrumb">Products</div>
    <div class="breadcrumb-rule"></div>
    <h1 class="page-title">Personality for your home</h1>
    <p class="intro">If your Searchly searches include words such as "beige", "off white" or "cream", then this is not the site for you. If you:Have a creative mind;Are bold and courageous;Have a sense of humour;Don't like your husband; or Are regretting what you have done with the last 20 years of your life;Then this site is for you.</p>
    <h2 class="feature-heading">Lorem ipsum dolor sit amet,</h2>
    <div class="dotted-rule"></div>

    <section class="service-card" style="left:44px;">
      <h2>Products</h2>
      <p>Lorem ipsum dolor sit amet, consectetuer adipiscing elit. Aenean commodo ligula eget dolor. Aenean massa. Cum sociis natoque penatibus et magnis dis parturient montes, nascetur ridiculus mus. Donec quam felis, ultricies nec, pellentesque eu, pretium.</p>
    </section>
    <section class="service-card" style="left:275px;">
      <h2>Consult</h2>
      <p>Lorem ipsum dolor sit amet, consectetuer adipiscing elit. Aenean commodo ligula eget dolor. Aenean massa. Cum sociis natoque penatibus et magnis dis parturient montes, nascetur ridiculus mus. Donec quam felis, ultricies nec, pellentesque eu, pretium.</p>
    </section>
    <section class="service-card" style="left:506px;">
      <h2>Decor</h2>
      <p>Lorem ipsum dolor sit amet, consectetuer adipiscing elit. Aenean commodo ligula eget dolor. Aenean massa. Cum sociis natoque penatibus et magnis dis parturient montes, nascetur ridiculus mus. Donec quam felis, ultricies nec, pellentesque eu.</p>
    </section>
  </main>

  <footer class="site-footer">
    <svg class="social-links" viewBox="0 0 80 24" aria-label="Social links">
      <circle cx="11" cy="12" r="11" fill="#3b5998"/>
      <circle cx="40" cy="12" r="11" fill="#1da1e2"/>
      <circle cx="68" cy="12" r="11" fill="#dd4b39"/>
    </svg>
    <div class="contact-block">
      CONTACT US:<br>
      PHONE: (555) 013 4821<br>
      ADDRESS: 48 Lantern Row, Coral Bay, FL 30310
    </div>
    <p class="footnote"><sup>1</sup> Applies to shipping within India. Information about shipping policies for other countries can be found here: <a href="#">Payment and Delivery Information</a></p>
    <p class="footer-links"><a href="#">About</a> | <a href="#">Payment and Delivery Information</a> | <a href="#">Print Version</a> | <a href="#">Sitemap</a></p>
    <a class="login-link" href="#">Login</a>
  </footer>
</body>
</html>
```